Velmorra Aviation - Insurance Brokers - Half page magazine ad.

Half-page ad in an aviation industry magazine promoting our services as an aviation insurance broker. I've attached an example of a pop-up banner we used at a conference recently to give you an idea.

I have attached a copy of the specifications from the publisher. Half-page ad requires:
- 190mm width x 132mm height
- Minimum 300 dpi
- colours in CMYK
- high resolution PDF with fonts embedded

Target Market(s)

Aircraft owners/operators, drone owners/operators, pilots

Font styles to use
Serif

Colors

Designer to choose colors to be used in the design.

Requirements
Must have
• 1. Company logo (attached).
• 2. Contact Details as follows:
• www.qtnaviation.com.au
• (02) 4193 7625
Nice to have
• Maybe a picture of an aircraft/helicopter in the bakground with logo/text etc over the top. But happy to look at alternative design options.

```html
<!DOCTYPE html>
<html lang="en">
<head>
<meta charset="utf-8">
<title>Velmorra Aviation – Specialist Aviation Insurance Brokers</title>
<link rel="stylesheet" href="https://fonts.googleapis.com/css2?family=Hind:wght@600&family=Roboto+Condensed:wght@700&display=swap">
<style>
  :root {
    --navy: #232a5c;
    --red: #d32031;
    --white: #ffffff;
    --stage: #000000;
    --sky-top: #7fa6d6;
    --sky-bottom: #c9dbef;
    --drone-top: #4f82c4;
    --drone-bottom: #d9dee6;
  }
  html, body {
    margin: 0;
    width: 1200px;
    height: 1200px;
    overflow: hidden;
    background: var(--stage);
  }
  .ad {
    position: absolute;
    left: 18px;
    top: 195px;
    width: 1164px;
    height: 808px;
    background: var(--white);
    overflow: hidden;
  }
  .ad-artwork {
    position: absolute;
    inset: 0;
  }
  .headline {
    position: absolute;
    right: 366px;
    top: 378px;
    margin: 0;
    font-family: "Hind", sans-serif;
    font-weight: 600;
    font-size: 52px;
    line-height: 62px;
    letter-spacing: 0.5px;
    color: var(--white);
    text-align: right;
  }
  .services {
    position: absolute;
    left: 838px;
    top: 382px;
    margin: 0;
    padding: 0;
    list-style: none;
    font-family: "Roboto Condensed", sans-serif;
    font-weight: 700;
    font-size: 35px;
    line-height: 44px;
    color: var(--white);
  }
  .services li {
    position: relative;
    padding-left: 22px;
  }
  .services li::before {
    content: "";
    position: absolute;
    left: 0;
    top: 19px;
    width: 8px;
    height: 8px;
    border-radius: 50%;
    background: var(--red);
  }
  .brand {
    position: absolute;
    left: 60px;
    top: 560px;
    display: flex;
    align-items: center;
    gap: 14px;
    font-family: "Hind", sans-serif;
    font-weight: 600;
    font-size: 44px;
    line-height: 1;
    color: var(--navy);
  }
  .brand-dot {
    width: 26px;
    height: 26px;
    border-radius: 50%;
    background: var(--red);
  }
  .contact {
    position: absolute;
    left: 50px;
    top: 672px;
    margin: 0;
    padding: 0;
    list-style: none;
    font-family: "Roboto Condensed", sans-serif;
    font-weight: 700;
    font-size: 38px;
    line-height: 46px;
    color: var(--navy);
  }
  .contact li {
    display: flex;
    align-items: center;
    gap: 18px;
  }
  .contact svg {
    width: 30px;
    height: 30px;
    flex: none;
  }
</style>
</head>
<body>
  <main class="ad">
    <svg class="ad-artwork" width="1164" height="808" viewBox="0 0 1164 808" xmlns="http://www.w3.org/2000/svg">
      <defs>
        <linearGradient id="sky" x1="0" y1="0" x2="0" y2="1">
          <stop offset="0" stop-color="var(--sky-top)"/>
          <stop offset="1" stop-color="var(--sky-bottom)"/>
        </linearGradient>
        <linearGradient id="drone-sky" x1="0" y1="0" x2="0" y2="1">
          <stop offset="0" stop-color="var(--drone-top)"/>
          <stop offset="1" stop-color="var(--drone-bottom)"/>
        </linearGradient>
      </defs>
      <polygon class="photo-aircraft" role="img" aria-label="Photo of a passenger jet landing against a cloudy blue sky"
               points="0,0 800,0 690,200 0,360" fill="url(#sky)"/>
      <polygon class="photo-drone" role="img" aria-label="Photo of a camera drone flying in front of snowy mountains"
               points="830,0 1164,0 1164,370 730,215" fill="url(#drone-sky)"/>
      <polygon class="panel-navy" points="400,455 720,235 1164,395 1164,808 880,808" fill="var(--navy)"/>
      <rect class="rule-navy" x="0" y="396" width="420" height="14" fill="var(--navy)"/>
      <rect class="rule-red" x="0" y="420" width="380" height="14" fill="var(--red)"/>
    </svg>

    <h1 class="headline">Specialist<br>Aviation<br>Insurance<br>Brokers</h1>

    <ul class="services">
      <li>Fixed Wing</li>
      <li>Rotorwing</li>
      <li>MRO’s</li>
      <li>Manufacturers</li>
      <li>Drones</li>
      <li>Loss of Licence</li>
      <li>Personal Accident</li>
    </ul>

    <div class="brand"><span class="brand-dot"></span>Velmorra Aviation</div>

    <ul class="contact">
      <li>
        <svg viewBox="0 0 30 30" aria-hidden="true">
          <g fill="none" stroke="var(--red)" stroke-width="2.4">
            <circle cx="15" cy="15" r="12"/>
            <ellipse cx="15" cy="15" rx="5.5" ry="12"/>
            <line x1="3" y1="15" x2="27" y2="15"/>
            <path d="M5,8.5 H25 M5,21.5 H25"/>
          </g>
        </svg>
        www.qtnaviation.com.au
      </li>
      <li>
        <svg viewBox="0 0 30 30" aria-hidden="true">
          <path fill="var(--red)" d="M8.2,3.5 L11.5,3 L14,9.5 L11.3,11.8 C12.6,15 15,17.4 18.2,18.7 L20.5,16 L27,18.5 L26.5,21.8 C26,24.6 23.6,26.5 20.8,26.2 C12,25.3 4.7,18 3.8,9.2 C3.5,6.4 5.4,4 8.2,3.5 Z"/>
        </svg>
        (02) 4193 7625
      </li>
    </ul>
  </main>
</body>
</html>
```